Flyer Templates, Business Card & Facebook Cover Image for New Fitness Company
Flyer Templates, Business Card & Facebook Cover Image for New Fitness Company  - Sports
Creative Brief
Please note the information below as more specific guidelines: Clean, fresh, design, please avoid using any images as the ones sourced do not reflect the 'Pulse Forge / Athletic' fitness I am targeting. Text to be arranged in different sizing/ blocking. All colours to be from the logos only. Flyer 1 - Black Background Main Text 'Attention Ladies - Strong is the New Skinny' Secondary Text 'Come and Discover Training Reimagined' Bullet Pointed - 'One to One Functional Assessments - Small Group Training - Fully Adaptable for Pre and Post Natal Mums' Logo in bottom right hand corner. Facebook, website, phone contact details. Flyer 2 - White Background Main Text - 1. Prevention, 2. Reversal, 3. Control Wake Up Everyday Stronger Than Yesterday Secondary Text 'Come and Discover Training Reimagined' Bullet Pointed - 'One to One Functional Assessments - Small Group Training - Fully Scalable for All Levels Logo in bottom right hand corner. Facebook, website, phone contact details. Flyer 3 - Black Background Main Text 'SWEAT is Just Fat Crying' 'Train Like an Athlete. Eat Like a Caveman. Get Results' Secondary Text 'Come and Discover Training Reimagined' Bullet Pointed - 'One to One Functional Assessments - Small Group Training - Body Transformation Bootcamps' Logo in bottom right hand corner. Learn More - Facebook, website, phone contact details. Flyer 4 - White Background Main Text 'Forget the Gym. The Fitness Playground has Arrived' Second Text 'FUNctional Parent and Kids After School Group Training' Bullet Pointed - Improve concentration, self esteem and strength Logo in bottom right hand corner Learn More - Facebook, website, phone contact details. Facebook Cover Image - Black Background. Logo Only with 'Discover Training Reimagined' in main text next to it and contact number. Business Card Logo, 'Discover Training Reimagined' text, Name, Email, Website, Phone number details
Sports
All files to be in editable format i.e. all text can be changed and edited with new text and images can be replaced. These are sample flyers - the idea is to gain a suitable template that can be modified for each marketing campaign. Facebook cover photo also need to be edit friendly.

```html
<!DOCTYPE html>
<html lang="en">
<head>
<meta charset="utf-8">
<title>Kinetic Rise Fitness – Business Cards</title>
<link rel="stylesheet" href="https://fonts.googleapis.com/css2?family=Roboto:wght@400;500;700&family=Roboto+Condensed:wght@700&family=Russo+One&display=swap">
<style>
  :root {
    --backdrop: #5a3b22;
    --card-dark: #0c0c0c;
    --card-light: #ffffff;
    --teal: #2a9a9c;
    --orange: #f08a24;
    --ink-light: #f2f2f2;
    --ink-dark: #2b2b2b;
  }
  html, body { margin: 0; padding: 0; }
  body {
    width: 1200px; height: 713px; overflow: hidden;
    background: var(--backdrop);
    position: relative;
    font-family: "Roboto", sans-serif;
  }
  .card {
    position: absolute; width: 542px; height: 324px;
    box-shadow: 0 4px 14px rgba(0,0,0,.45);
  }
  .card--dark { background: var(--card-dark); color: var(--ink-light); }
  .card--light { background: var(--card-light); color: var(--ink-dark); }
  .card--front-dark { left: 29px; top: 19px; }
  .card--front-light { left: 619px; top: 19px; }
  .card--back-dark { left: 29px; top: 365px; }
  .card--back-light { left: 619px; top: 365px; }

  .brand {
    position: absolute; left: 0; right: 0; top: 34px;
    display: flex; flex-direction: column; align-items: center; gap: 8px;
  }
  .brand__mark { width: 70px; height: 70px; border-radius: 50%; background: var(--teal); }
  .brand__name {
    font-family: "Roboto Condensed", sans-serif; font-weight: 700;
    font-size: 30px; color: var(--teal); letter-spacing: .3px; line-height: 1;
  }

  .person { position: absolute; left: 0; width: 258px; top: 178px; text-align: right; }
  .person__name { font-size: 23px; color: var(--teal); font-weight: 500; }
  .person__title { font-size: 13px; color: var(--orange); margin-top: 2px; }
  .person__address { font-size: 13px; margin-top: 10px; line-height: 1.45; }

  .contacts {
    position: absolute; left: 278px; top: 174px; margin: 0; padding: 0;
    list-style: none; font-size: 12.5px; line-height: 22px;
  }
  .contacts li { display: flex; align-items: center; gap: 8px; }
  .contacts__icon { width: 11px; height: 11px; background: currentColor; opacity: .85; border-radius: 2px; flex: none; }
  .contacts__icon--round { border-radius: 50%; }

  .hero {
    position: absolute; left: 0; right: 0; top: 42px;
    display: flex; align-items: center; justify-content: center; gap: 16px;
  }
  .hero__mark { width: 120px; height: 120px; border-radius: 50%; background: var(--teal); }
  .hero__name {
    font-family: "Roboto Condensed", sans-serif; font-weight: 700;
    font-size: 40px; line-height: 1.05; color: var(--orange);
  }
  .tagline {
    position: absolute; left: 0; right: 0; top: 246px; text-align: center;
    font-family: "Russo One", sans-serif; font-size: 24px; letter-spacing: 2px; color: var(--teal);
  }
  .card--back-light .tagline { top: 206px; font-size: 22px; }
  .socials {
    position: absolute; left: 0; right: 0; top: 256px;
    display: flex; justify-content: center; gap: 22px; font-size: 12.5px;
  }
  .socials span { display: flex; align-items: center; gap: 6px; }
  .website { position: absolute; left: 0; right: 0; top: 284px; text-align: center; font-size: 13px; letter-spacing: 2px; }
</style>
</head>
<body>

  <section class="card card--dark card--front-dark">
    <div class="brand">
      <div class="brand__mark"></div>
      <div class="brand__name">Kinetic Rise Fitness</div>
    </div>
    <div class="person">
      <div class="person__name">Your Name</div>
      <div class="person__title">Title</div>
      <div class="person__address">00, Complex name<br>City, State 0042</div>
    </div>
    <ul class="contacts">
      <li><span class="contacts__icon"></span>0123 456789</li>
      <li><span class="contacts__icon"></span>info@kineticrise.com</li>
      <li><span class="contacts__icon contacts__icon--round"></span>www.kineticrise.com</li>
      <li><span class="contacts__icon"></span>kineticrise.com</li>
      <li><span class="contacts__icon"></span>kineticrise.com</li>
    </ul>
  </section>

  <section class="card card--light card--front-light">
    <div class="brand">
      <div class="brand__mark"></div>
      <div class="brand__name">Kinetic Rise Fitness</div>
    </div>
    <div class="person">
      <div class="person__name">Your Name</div>
      <div class="person__title">Title</div>
      <div class="person__address">00, Complex name<br>City, State 0042</div>
    </div>
    <ul class="contacts">
      <li><span class="contacts__icon"></span>0123 456789</li>
      <li><span class="contacts__icon"></span>info@kineticrise.com</li>
      <li><span class="contacts__icon contacts__icon--round"></span>www.kineticrise.com</li>
      <li><span class="contacts__icon"></span>kineticrise.com</li>
      <li><span class="contacts__icon"></span>kineticrise.com</li>
    </ul>
  </section>

  <section class="card card--dark card--back-dark">
    <div class="hero">
      <div class="hero__mark"></div>
      <div class="hero__name">Kinetic Rise<br>Fitness</div>
    </div>
    <div class="tagline">Discover Training Reimagined</div>
  </section>

  <section class="card card--light card--back-light">
    <div class="hero">
      <div class="hero__mark"></div>
      <div class="hero__name">Kinetic Rise<br>Fitness</div>
    </div>
    <div class="tagline">Discover Training Reimagined</div>
    <div class="socials">
      <span><span class="contacts__icon"></span>kineticrise.com</span>
      <span><span class="contacts__icon"></span>kineticrise.com</span>
    </div>
    <div class="website">www.Kineticrise.com</div>
  </section>

</body>
</html>
```